Postcard Design

We are a full service lawn and landscape maintenance business. Employees are myself as owner-operator and
my son as operator and pesticide applicator and hardscape designer and builder along with myself as helper in the
hardscape. We have over 30 years experience and have operated as Doug's Yard Trimming for 23 years since 1993.
We are dependable and reasonably priced and hard working. My son is an excellent operator. We are full service year round. Spring cleanups, Summer all service, Fall cleanups and Winter snow removal.

Industry/Entity Type

Business

```html
<!DOCTYPE html>
<html lang="en">
<head>
<meta charset="utf-8">
<title>Doug's Yard Trimming – Postcard</title>
<link rel="stylesheet" href="https://fonts.googleapis.com/css2?family=Oswald:wght@400;500&family=Montserrat:wght@700&family=Arimo:wght@400;700&display=swap">
<style>
  :root{
    --page:#ecebe7;
    --forest:#1e3426;
    --brand-green:#5a9a2e;
    --head-green:#3f6b2a;
    --accent-green:#a5d86a;
    --cream:#f6efbf;
    --red:#c0241f;
    --red-dark:#7d1512;
    --white:#ffffff;
    --lawn-1:#4f8f2a;
    --lawn-2:#2f6a1c;
  }
  *{box-sizing:border-box;margin:0;padding:0}
  html,body{width:1200px;height:1000px;overflow:hidden}
  body{background:var(--page);position:relative;font-family:"Arimo",Arial,sans-serif}

  .card{position:absolute;width:713px;height:462px;overflow:hidden;background:var(--forest);box-shadow:0 4px 14px rgba(0,0,0,.25)}
  .card--front{left:37px;top:30px}
  .card--back{left:428px;top:506px}
  .card svg.shapes{position:absolute;inset:0}

  .abs{position:absolute}
  .brand{font-family:"Montserrat",Arial,sans-serif;font-weight:700;color:var(--brand-green);line-height:1}
  .brand__name{display:block;font-size:66px;letter-spacing:-1px}
  .brand__sub{display:block;font-size:20px;margin-top:6px}

  .front-brand{left:30px;top:26px}
  .front-headline{left:29px;top:162px;font-family:"Oswald",sans-serif;font-weight:500;font-size:33px;line-height:39px;color:var(--head-green);text-transform:uppercase}
  .front-experience{left:10px;top:361px;width:240px;text-align:center;font-weight:700;font-size:17.5px;line-height:22px;color:var(--white)}
  .front-call{left:352px;top:28px;font-family:"Oswald",sans-serif;color:var(--white);font-size:21px;white-space:nowrap}
  .front-call strong{font-weight:500;font-size:35px;color:var(--cream);margin-left:6px;vertical-align:-3px}
  .front-tagline{left:252px;top:410px;width:445px;text-align:center;font-family:"Oswald",sans-serif;font-size:21px;color:var(--white)}

  .snapshot{position:absolute;background:var(--white);padding:6px;box-shadow:0 2px 6px rgba(0,0,0,.35)}
  .snapshot div{width:100%;height:100%}
  .snapshot--rake{left:26px;top:22px;width:170px;height:137px;transform:rotate(-4deg)}
  .snapshot--rake div{background:linear-gradient(160deg,#6f8f3a,#b8872f 65%,#7b6a2a)}
  .snapshot--blower{left:168px;top:68px;width:176px;height:140px;transform:rotate(3deg)}
  .snapshot--blower div{background:linear-gradient(200deg,#4c6a36,#c86a2a 60%,#8a4a22)}

  .back-brand{left:404px;top:72px;text-align:center}
  .back-brand .brand__name{font-size:44px;color:var(--accent-green)}
  .back-brand .brand__sub{font-size:14px;color:var(--accent-green)}
  .back-call{left:420px;top:142px;width:152px;text-align:center;font-family:"Oswald",sans-serif;color:var(--white);font-size:16px;line-height:22px}
  .back-call strong{display:block;font-weight:500;font-size:25px;line-height:32px;color:var(--cream)}
  .back-about{left:36px;top:220px;width:190px;font-size:13px;line-height:16.3px;color:var(--white)}
  .back-about em{font-style:normal;color:var(--cream)}
  .back-about p+p{margin-top:16px}
  .services{left:248px;top:218px;font-family:"Oswald",sans-serif;color:var(--white)}
  .services h2{font-weight:500;font-size:26px;color:var(--accent-green);text-transform:uppercase;margin-bottom:4px}
  .services li{list-style:none;font-size:21px;line-height:32.5px;display:flex;align-items:center;gap:8px}
  .services svg{width:14px;height:14px}
  .stamp{left:599px;top:11px;width:103px;height:102px;background:var(--white)}
</style>
</head>
<body>

<section class="card card--front" aria-label="Postcard front">
  <svg class="shapes" width="713" height="462" viewBox="0 0 713 462">
    <defs>
      <linearGradient id="panelFade" x1="0" y1="0" x2="0" y2="1">
        <stop offset="0" stop-color="#ffffff"/>
        <stop offset="1" stop-color="#b9d6a4"/>
      </linearGradient>
      <linearGradient id="redBlock" x1="0" y1="0" x2="1" y2="0">
        <stop offset="0" stop-color="var(--red-dark)"/>
        <stop offset=".55" stop-color="var(--red)"/>
        <stop offset="1" stop-color="var(--red-dark)"/>
      </linearGradient>
      <linearGradient id="frontLawn" x1="0" y1="0" x2="0" y2="1">
        <stop offset="0" stop-color="#3d6f25"/>
        <stop offset=".35" stop-color="var(--lawn-1)"/>
        <stop offset="1" stop-color="var(--lawn-2)"/>
      </linearGradient>
    </defs>
    <rect x="290" y="85" width="423" height="310" fill="url(#frontLawn)" role="img" aria-label="Photo of a person on a red riding mower cutting a striped lawn"/>
    <polygon points="0,0 343,0 228,462 0,462" fill="url(#panelFade)"/>
    <polygon points="0,345 255,345 225,462 0,462" fill="url(#redBlock)"/>
  </svg>

  <div class="abs brand front-brand">
    <span class="brand__name">Doug's</span>
    <span class="brand__sub">Yard Trimming</span>
  </div>
  <h1 class="abs front-headline">Full service lawn<br>and landscape<br>maintenance<br>business</h1>
  <p class="abs front-experience">30 years experience and have operated for 23 years since 1993.</p>
  <p class="abs front-call">Call Us Today at <strong>444-555-0182</strong></p>
  <p class="abs front-tagline">Dependable, Reasonably Priced And Hard Working</p>
</section>

<section class="card card--back" aria-label="Postcard back">
  <svg class="shapes" width="713" height="462" viewBox="0 0 713 462">
    <defs>
      <linearGradient id="backLawn" x1="0" y1="0" x2="0" y2="1">
        <stop offset="0" stop-color="#2f5e22"/>
        <stop offset=".45" stop-color="#4e9a2c"/>
        <stop offset="1" stop-color="#3c8a22"/>
      </linearGradient>
    </defs>
    <rect x="0" y="0" width="713" height="203" fill="url(#backLawn)" role="img" aria-label="Photo of a landscaped garden with trimmed shrubs and lawn"/>
    <rect x="472" y="203" width="241" height="259" fill="var(--white)"/>
    <rect x="309" y="399" width="404" height="63" fill="var(--white)"/>
  </svg>

  <figure class="snapshot snapshot--rake"><div role="img" aria-label="Photo of a wheelbarrow full of autumn leaves and a rake"></div></figure>
  <figure class="snapshot snapshot--blower"><div role="img" aria-label="Photo of a worker clearing autumn leaves with a blower"></div></figure>

  <div class="abs stamp" aria-label="Stamp area"></div>

  <div class="abs brand back-brand">
    <span class="brand__name">Doug's</span>
    <span class="brand__sub">Yard Trimming</span>
  </div>
  <p class="abs back-call">Call Us Today at <strong>444-555-0182</strong></p>

  <div class="abs back-about">
    <p>Employees are myself as owner-operator and my son as operator and <em>Pesticide Applicator and Hardscape Designer and Builder</em> along with myself as helper in the Hardscape.</p>
    <p>We have over 30 years experience and have operated as Doug's Yard Trimming for 23 years</p>
  </div>

  <div class="abs services">
    <h2>Services Offered</h2>
    <ul>
      <li><svg viewBox="0 0 14 14"><rect x=".5" y=".5" width="13" height="13" fill="none" stroke="#fff"/><path d="M3 7l3 3 6-8" fill="none" stroke="#fff" stroke-width="2"/></svg>Spring Cleanups</li>
      <li><svg viewBox="0 0 14 14"><rect x=".5" y=".5" width="13" height="13" fill="none" stroke="#fff"/><path d="M3 7l3 3 6-8" fill="none" stroke="#fff" stroke-width="2"/></svg>Summer All Service</li>
      <li><svg viewBox="0 0 14 14"><rect x=".5" y=".5" width="13" height="13" fill="none" stroke="#fff"/><path d="M3 7l3 3 6-8" fill="none" stroke="#fff" stroke-width="2"/></svg>Fall Cleanups</li>
      <li><svg viewBox="0 0 14 14"><rect x=".5" y=".5" width="13" height="13" fill="none" stroke="#fff"/><path d="M3 7l3 3 6-8" fill="none" stroke="#fff" stroke-width="2"/></svg>Winter Snow Removal.</li>
    </ul>
  </div>
</section>

</body>
</html>
```